Design some Business Cards for Real Estate Company

This is the contest I ran last year. I like #176
https://www.briefgallop.example/contest/Design-Business-Card-for-NYC-Real-Estate-Firm-83917.html

Looking for:
Clean, sexy, chic card
One side white
Horizontal

*DON'T: write "email" or "phone" - Don't have a picture of phone or email sign*

FRONT OF THE CARD: If you want to put a logo, have it watermarked
COLOR: see attached
NAME: Miriam Faye Quillerby, Founder
SMALL FONT SIZE: Licensed Real Estate Broker
ADDRESS: 4806 Larkspur Boulevard, 17th Floor, New York, New York 10036
EMAIL: miriam@[url removed, login to view]
WEBSITE (don't include www): [url removed, login to view]
PHONE: c 212.555.7314 (include the 'c' for cell)
PHONE: o 212.555.9062 (include the 'o' for office)
SOCIAL
[url removed, login to view]

BACK OF THE CARD
LOGO: see attached (horizontal)
CENTERED TEXT: Investing | Brokerage | New Development | Management

```html
<!DOCTYPE html>
<html lang="en">
<head>
<meta charset="utf-8">
<title>Larkmont Properties International – Business Card</title>
<link rel="stylesheet" href="https://fonts.googleapis.com/css2?family=Open+Sans:wght@400;600;700&display=swap">
<style>
  :root {
    --page: #e9eaec;
    --card-white: #ffffff;
    --charcoal-dark: #23262b;
    --charcoal: #3a3e45;
    --ink: #2b2f35;
    --ink-soft: #5b626b;
    --blue-deep: #0b5fb0;
    --blue: #1f8fe0;
    --blue-light: #5cc0ff;
    --silver: #cfd6dd;
    --white: #ffffff;
  }
  * { margin: 0; padding: 0; box-sizing: border-box; }
  html, body {
    width: 1200px; height: 912px; overflow: hidden;
    background: var(--page);
    font-family: "Open Sans", Arial, sans-serif;
  }
  .sheet {
    width: 1200px; height: 912px;
    display: flex; flex-direction: column; align-items: center; justify-content: center;
    gap: 30px;
  }
  .card {
    position: relative; width: 720px; height: 411px;
    border-radius: 6px; overflow: hidden;
    box-shadow: 0 6px 18px rgba(0,0,0,0.22);
  }
  .card-art { position: absolute; inset: 0; }

  /* Contact side (white) */
  .card-front { background: var(--card-white); color: var(--ink); }
  .identity { position: absolute; left: 40px; top: 150px; }
  .identity-name { font-size: 28px; font-weight: 700; color: var(--ink); line-height: 1.2; }
  .identity-title { font-size: 15px; font-weight: 600; color: var(--blue-deep); margin-top: 2px; }
  .identity-licence { font-size: 12px; color: var(--ink-soft); }

  .contact-list { position: absolute; left: 420px; top: 160px; width: 270px; list-style: none; }
  .contact-list li { font-size: 13px; line-height: 18px; color: var(--ink); margin-bottom: 12px; }
  .contact-list .contact-prefix { font-weight: 700; color: var(--blue-deep); margin-right: 4px; }

  .social-list { position: absolute; left: 40px; top: 282px; list-style: none; }
  .social-list li {
    display: flex; align-items: center; gap: 12px;
    font-size: 13px; line-height: 18px; color: var(--ink); margin-bottom: 14px;
  }
  .social-tile { width: 20px; height: 20px; border-radius: 4px; background: var(--charcoal); }

  /* Brand side */
  .card-back { color: var(--white); }
  .brand { position: absolute; left: 92px; top: 190px; display: flex; align-items: center; gap: 18px; }
  .brand-mark { width: 60px; height: 60px; border-radius: 50%; background: var(--white); }
  .brand-name { font-weight: 400; text-transform: uppercase; line-height: 1; }
  .brand-name .line-main { display: block; font-size: 40px; letter-spacing: 1px; }
  .brand-name .line-sub { display: block; font-size: 14px; letter-spacing: 1.5px; margin-top: 6px; }
  .services {
    position: absolute; left: 0; right: 0; top: 292px;
    text-align: center; font-size: 14px; font-weight: 600; letter-spacing: 0.5px;
  }
</style>
</head>
<body>
<main class="sheet">

  <section class="card card-front" aria-label="Business card, contact side">
    <svg class="card-art" viewBox="0 0 720 411" aria-hidden="true">
      <defs>
        <linearGradient id="front-blue" x1="0" y1="0" x2="1" y2="0.3">
          <stop offset="0" stop-color="var(--blue-deep)"/>
          <stop offset="0.6" stop-color="var(--blue)"/>
          <stop offset="1" stop-color="var(--blue-light)"/>
        </linearGradient>
      </defs>
      <path d="M0 0 H720 V30 C560 40 440 70 360 90 C260 114 140 122 0 122 Z" fill="url(#front-blue)"/>
      <path d="M0 122 C140 122 260 114 360 90 C440 70 560 40 720 30 V38 C560 48 442 78 362 98 C262 122 142 130 0 130 Z" fill="var(--silver)"/>
      <path d="M0 130 C142 130 262 122 362 98 C442 78 560 48 720 38 V42 C560 53 444 83 364 103 C264 127 144 135 0 135 Z" fill="var(--blue)"/>
      <rect x="0" y="396" width="720" height="15" fill="var(--charcoal)"/>
    </svg>

    <div class="identity">
      <h1 class="identity-name">Miriam Faye Quillerby</h1>
      <p class="identity-title">Founder</p>
      <p class="identity-licence">Licensed Real Estate Broker</p>
    </div>

    <ul class="contact-list">
      <li>4806 Larkspur Boulevard, 17th Floor, New York, New York 10036</li>
      <li>miriam@larkmont.example</li>
      <li>larkmont.example</li>
      <li><span class="contact-prefix">c</span>212.555.7314</li>
      <li><span class="contact-prefix">o</span>212.555.9062</li>
    </ul>

    <ul class="social-list">
      <li><span class="social-tile"></span><span>snapfeed.example/lpinyc</span></li>
      <li><span class="social-tile"></span><span>clipcast.example/lpinyc</span></li>
      <li><span class="social-tile"></span><span>friendwall.example/lpinyc</span></li>
    </ul>
  </section>

  <section class="card card-back" aria-label="Business card, brand side">
    <svg class="card-art" viewBox="0 0 720 411" aria-hidden="true">
      <defs>
        <linearGradient id="back-dark" x1="0" y1="0" x2="1" y2="1">
          <stop offset="0" stop-color="var(--charcoal)"/>
          <stop offset="1" stop-color="var(--charcoal-dark)"/>
        </linearGradient>
        <linearGradient id="back-blue" x1="0" y1="1" x2="1" y2="0">
          <stop offset="0" stop-color="var(--blue-deep)"/>
          <stop offset="0.55" stop-color="var(--blue)"/>
          <stop offset="1" stop-color="var(--blue-light)"/>
        </linearGradient>
      </defs>
      <rect width="720" height="411" fill="url(#back-dark)"/>
      <path d="M0 330 C150 300 230 230 330 150 C430 75 560 40 720 35 V330 C590 330 480 350 390 380 C320 403 240 411 180 411 H0 Z" fill="url(#back-blue)"/>
      <path d="M0 322 C150 292 228 222 328 142 C430 66 560 30 720 25 V35 C560 40 430 75 330 150 C230 230 150 300 0 330 Z" fill="var(--silver)"/>
      <path d="M180 411 C240 411 320 403 390 380 C480 350 590 330 720 330 V344 C595 344 486 362 396 392 C350 406 300 411 260 411 Z" fill="var(--silver)"/>
    </svg>

    <div class="brand">
      <span class="brand-mark"></span>
      <p class="brand-name">
        <span class="line-main">Larkmont</span>
        <span class="line-sub">Properties International</span>
      </p>
    </div>
    <p class="services">Investing | Brokerage | New Development | Management</p>
  </section>

</main>
</body>
</html>
```